Harborline Supply Company Business Card Design

The Business Card will be one side only with Harborline Supplies Company Logo
Card should have:
Name
Title
Office phone Number
Cell Number
email address
Website
Street Address
Our Slogan is Rugged and Reliable
Looking for something that stands out from other business cards

Target Market(s)

Heavy equipment Lease Company

```html
<!DOCTYPE html>
<html lang="en">
<head>
<meta charset="utf-8">
<title>Harborline Supplies Company – Business Card</title>
<link href="https://fonts.googleapis.com/css2?family=Lato:ital,wght@0,400;0,700;1,700&display=swap" rel="stylesheet">
<style>
  :root {
    --navy: #262a78;
    --navy-deep: #1f2366;
    --red: #d4102e;
    --ink: #4a4a4a;
    --paper: #ffffff;
    --backdrop: #ecebe8;
  }
  * { margin: 0; padding: 0; box-sizing: border-box; }
  html, body {
    width: 1200px; height: 870px; overflow: hidden;
    background: var(--backdrop);
    font-family: "Lato", Arial, sans-serif;
  }
  .card {
    position: absolute; left: 50px; top: 121px;
    width: 1100px; height: 627px;
    background: var(--paper);
    overflow: hidden;
    box-shadow: 0 2px 8px rgba(0,0,0,0.12);
  }
  .brand {
    position: absolute; left: 103px; top: 264px;
    display: flex; align-items: center; gap: 14px;
  }
  .brand-dot {
    width: 44px; height: 44px; border-radius: 50%;
    background: var(--navy);
  }
  .brand-name {
    color: var(--navy); font-weight: 700; font-size: 25px;
    letter-spacing: 0.2px;
  }
  .contact { position: absolute; left: 615px; top: 128px; }
  .person-name {
    color: var(--navy); font-weight: 700; font-size: 42px;
    line-height: 1; letter-spacing: 0.5px;
  }
  .person-title {
    color: var(--red); font-size: 26px; line-height: 1;
    margin-top: 6px; letter-spacing: 0.3px;
  }
  .address {
    color: var(--ink); font-size: 24px; line-height: 30px;
    margin-top: 22px;
  }
  .details { list-style: none; margin-top: 16px; }
  .details li {
    display: flex; align-items: center; gap: 14px;
    color: var(--ink); font-size: 24px; height: 35px;
  }
  .details svg { width: 24px; height: 24px; fill: var(--navy); flex: none; }
  .footer-band {
    position: absolute; left: 0; bottom: 0;
    width: 1100px; height: 107px;
    background: linear-gradient(90deg, var(--navy) 0%, var(--navy-deep) 100%);
  }
  .slogan {
    position: absolute; left: 144px; top: 559px;
    color: #fff; font-weight: 700; font-style: italic; font-size: 27px;
  }
</style>
</head>
<body>
  <div class="card">
    <div class="footer-band" role="img" aria-label="Decorative red and navy wave band along the bottom edge"></div>

    <div class="brand">
      <span class="brand-dot"></span>
      <span class="brand-name">Harborline Supplies Company</span>
    </div>

    <div class="contact">
      <h1 class="person-name">MARCUS HALE</h1>
      <p class="person-title">CEO/FOUNDER</p>
      <p class="address">4120 Tidewater Road<br>Bayport, Alaska 34590</p>
      <ul class="details">
        <li>
          <svg viewBox="0 0 24 24"><path d="M6.6 10.8a15.1 15.1 0 0 0 6.6 6.6l2.2-2.2a1 1 0 0 1 1-.25 11.4 11.4 0 0 0 3.6.57 1 1 0 0 1 1 1V20a1 1 0 0 1-1 1A17 17 0 0 1 3 4a1 1 0 0 1 1-1h3.5a1 1 0 0 1 1 1c0 1.250.2 2.450.57 3.57a1 1 0 0 1-.25 1z"/></svg>
          555 214 7730
        </li>
        <li>
          <svg viewBox="0 0 24 24"><path d="M7 1h10a2 2 0 0 1 2 2v18a2 2 0 0 1-2 2H7a2 2 0 0 1-2-2V3a2 2 0 0 1 2-2zm0 3v14h10V4zm5 15.5a1 1 0 1 0 0 2 1 1 0 0 0 0-2z"/></svg>
          555 382 6194
        </li>
        <li>
          <svg viewBox="0 0 24 24"><path d="M2 6h20v13H2zm2 2v.4l8 5 8-5V8l-8 5z"/></svg>
          marcus@harborlinesupplies.com
        </li>
        <li>
          <svg viewBox="0 0 24 24"><path d="M12 2a10 10 0 1 0 0 20 10 10 0 0 0 0-20zm-1 17.9A8 8 0 0 1 4.2 10.6L9 15.4v1a2 2 0 0 0 2 2zm6.9-2.5A2 2 0 0 0 16 16h-1v-3a1 1 0 0 0-1-1H8v-2h2a1 1 0 0 0 1-1V7h2a2 2 0 0 0 2-2v-.4a8 8 0 0 1 2.9 12.8z"/></svg>
          harborlinesupplies.com
        </li>
      </ul>
    </div>

    <p class="slogan">Rugged &amp; Reliable</p>
  </div>
</body>
</html>
```